Offer banner redesign / Simplifying existing banner

We have a banner there customer can click on to get an offer. We want to simplify this banner and to get it to at minimum. We are not clear about how it shoulderstand look like, but the actual banner you can see here (It's at the top of the page): https://ofenrohr-lagerhaus.de/kaminsysteme/ We want to get rid of the icons and to reduce the size of the baner. The baner shoulderstand contain the Following text: Affordable chimney using installation service button text: Request free quote

Target Market(s)

Customers from age of 40yrs.

Requirements
Must have
• Clear and good visible button
Nice to have
• It Should be simple and striking.

```html
<!DOCTYPE html>
<html lang="de">
<head>
<meta charset="utf-8">
<title>Angebotsbanner Schornstein</title>
<link rel="stylesheet" href="https://fonts.googleapis.com/css2?family=Source+Sans+3:wght@400;600&display=swap">
<style>
  :root {
    --page-white: #ffffff;
    --stage-grey: #e6e7e9;
    --photo-sky: #8e969e;
    --photo-wood: #a8978a;
    --photo-ground: #6f6c68;
    --headline: #ffffff;
    --cta-light: #f4b236;
    --cta-dark: #e3901b;
    --cta-arrow: #d98316;
    --cta-text: #ffffff;
  }
  html, body {
    margin: 0;
    padding: 0;
    width: 1200px;
    height: 803px;
    overflow: hidden;
    background: var(--page-white);
    font-family: "Source Sans 3", "Myriad Pro", sans-serif;
  }
  .stage {
    position: absolute;
    left: 0;
    top: 125px;
    width: 1200px;
    height: 541px;
    background: var(--stage-grey);
  }
  .offer-banner {
    position: absolute;
    left: 92px;
    top: 144px;
    width: 997px;
    height: 267px;
  }
  .offer-banner::after {
    content: "";
    position: absolute;
    left: 12px;
    right: 12px;
    bottom: -14px;
    height: 18px;
    border-radius: 50%;
    background: rgba(0, 0, 0, 0.28);
    filter: blur(6px);
    z-index: 0;
  }
  .banner-photo {
    position: absolute;
    inset: 0;
    z-index: 1;
    background:
      linear-gradient(90deg, rgba(0,0,0,0) 0%, rgba(0,0,0,0) 55%, rgba(40,46,38,0.55) 75%, rgba(40,46,38,0.35) 100%),
      linear-gradient(180deg, var(--photo-sky) 0%, #99928c 30%, var(--photo-wood) 55%, #9c8a7c 85%, var(--photo-ground) 100%);
  }
  .banner-photo::before {
    content: "";
    position: absolute;
    inset: 0;
    background: rgba(30, 34, 40, 0.18);
  }
  .banner-copy {
    position: absolute;
    left: 533px;
    top: 17px;
    z-index: 2;
  }
  .headline {
    margin: 0;
    color: var(--headline);
    font-weight: 600;
    font-size: 26px;
    line-height: 32px;
    letter-spacing: 0.1px;
    text-shadow: 0 1px 3px rgba(0, 0, 0, 0.35);
  }
  .cta {
    position: relative;
    display: block;
    margin-top: 10px;
    width: 224px;
    height: 35px;
    text-decoration: none;
  }
  .cta svg {
    position: absolute;
    inset: 0;
  }
  .cta-label {
    position: absolute;
    left: 6px;
    top: 0;
    line-height: 35px;
    color: var(--cta-text);
    font-size: 11px;
    font-weight: 400;
    letter-spacing: -0.15px;
    white-space: nowrap;
    text-shadow: 0 1px 1px rgba(120, 60, 0, 0.35);
  }
</style>
</head>
<body>
  <div class="stage">
    <section class="offer-banner">
      <div class="banner-photo" role="img" aria-label="Foto: modernes Holzhaus mit Edelstahlschornstein und kleinem Nebengebäude in der Abenddämmerung, Bäume im Hintergrund"></div>
      <div class="banner-copy">
        <h1 class="headline">Preiswerter Schornstein<br>wahlweise mit Montageservice</h1>
        <a class="cta" href="#angebot">
          <svg width="224" height="35" viewBox="0 0 224 35" aria-hidden="true">
            <defs>
              <linearGradient id="cta-fill" x1="0" y1="0" x2="0" y2="1">
                <stop offset="0" stop-color="var(--cta-light)"/>
                <stop offset="1" stop-color="var(--cta-dark)"/>
              </linearGradient>
            </defs>
            <rect x="0" y="0" width="183" height="35" rx="2" fill="url(#cta-fill)"/>
            <path d="M183 0 H211 L224 17.5 L211 35 H183 Z" fill="var(--cta-arrow)"/>
            <path d="M183 0 H211 L224 17.5 L211 35 H183 Z" fill="url(#cta-fill)" opacity="0.55"/>
            <path d="M194 11.5 L200 17.5 L194 23.5 M201 11.5 L207 17.5 L201 23.5" fill="none" stroke="#ffffff" stroke-width="2.4" stroke-linecap="round" stroke-linejoin="round"/>
          </svg>
          <span class="cta-label">KOSTENLOSES ANGEBOT ANFORDERN</span>
        </a>
      </div>
    </section>
  </div>
</body>
</html>
```